Ridgeline Journeys business card

please see website
www.ridgelinejourneys.comau

info needed on card
Kieran Folsby
Ph
email
Adventure Riding GPS trails

please use my logo and colours off my site

Industry/Entity Type

Business

Contact Information for Business Card

Kieran Folsby
kieran@ridgelinejourneys.com

```html
<!DOCTYPE html>
<html lang="en">
<head>
<meta charset="utf-8">
<title>Ridgeline Journeys – Business Card</title>
<link href="https://fonts.googleapis.com/css2?family=Josefin+Sans:wght@400;700&display=swap" rel="stylesheet">
<style>
  :root {
    --backdrop: #ececec;
    --card: #ffffff;
    --ink: #141414;
    --accent: #f2d40c;
  }
  * { box-sizing: border-box; margin: 0; padding: 0; }
  html, body {
    width: 1200px;
    height: 800px;
    overflow: hidden;
    background: var(--backdrop);
    font-family: "Josefin Sans", "Helvetica Neue", Arial, sans-serif;
    color: var(--ink);
  }
  .business-card {
    position: absolute;
    left: 410px;
    top: 100px;
    width: 380px;
    height: 600px;
    background: var(--card);
    box-shadow: 0 12px 30px rgba(0,0,0,0.08);
    padding: 56px 40px 0 48px;
  }
  .brand {
    display: flex;
    align-items: center;
    gap: 14px;
    margin-left: 10px;
  }
  .brand-dot {
    width: 44px;
    height: 44px;
    border-radius: 50%;
    background: var(--accent);
    flex: none;
  }
  .brand-name {
    font-weight: 700;
    font-size: 24px;
    line-height: 1.05;
    text-transform: uppercase;
    letter-spacing: 0.5px;
    color: var(--ink);
  }
  .person-name {
    margin-top: 44px;
    margin-left: 10px;
    font-weight: 700;
    font-size: 40px;
    line-height: 1.05;
    letter-spacing: 2px;
    text-transform: uppercase;
  }
  .name-rule {
    width: 32px;
    height: 2px;
    background: var(--ink);
    margin: 14px 0 0 10px;
  }
  .contact-list {
    list-style: none;
    margin-top: 40px;
  }
  .contact-item {
    display: flex;
    align-items: center;
    gap: 22px;
    margin-bottom: 34px;
    font-size: 15px;
    line-height: 1.35;
  }
  .contact-icon {
    width: 40px;
    height: 40px;
    flex: none;
  }
</style>
</head>
<body>
  <article class="business-card">
    <header class="brand">
      <span class="brand-dot" aria-hidden="true"></span>
      <span class="brand-name">Ridgeline<br>Journeys</span>
    </header>

    <h1 class="person-name">Kieran<br>Folsby</h1>
    <div class="name-rule"></div>

    <ul class="contact-list">
      <li class="contact-item">
        <svg class="contact-icon" viewBox="0 0 40 40" aria-hidden="true">
          <polygon points="20,2 36,11 36,29 20,38 4,29 4,11" fill="none" stroke="#141414" stroke-width="3"/>
          <rect x="12" y="17" width="16" height="9" rx="2" fill="none" stroke="#141414" stroke-width="1.6"/>
          <path d="M11 17 q9 -7 18 0" fill="none" stroke="#141414" stroke-width="1.6"/>
          <circle cx="20" cy="21.5" r="2" fill="none" stroke="#141414" stroke-width="1.2"/>
        </svg>
        <span>123 456 789</span>
      </li>
      <li class="contact-item">
        <svg class="contact-icon" viewBox="0 0 40 40" aria-hidden="true">
          <polygon points="20,2 36,11 36,29 20,38 4,29 4,11" fill="none" stroke="#141414" stroke-width="3"/>
          <circle cx="20" cy="20" r="7" fill="none" stroke="#141414" stroke-width="1.5"/>
          <ellipse cx="20" cy="20" rx="3" ry="7" fill="none" stroke="#141414" stroke-width="1.2"/>
          <line x1="13" y1="20" x2="27" y2="20" stroke="#141414" stroke-width="1.2"/>
        </svg>
        <span>kieran@ridgelinejourneys.com<br>www.ridgelinejourneys.comau</span>
      </li>
      <li class="contact-item">
        <svg class="contact-icon" viewBox="0 0 40 40" aria-hidden="true">
          <polygon points="20,2 36,11 36,29 20,38 4,29 4,11" fill="none" stroke="#141414" stroke-width="3"/>
          <path d="M20 28 C15 22 15 19 15 18 a5 5 0 0 1 10 0 c0 1 0 4 -5 10 z" fill="none" stroke="#141414" stroke-width="1.5"/>
          <circle cx="20" cy="18" r="1.8" fill="#141414"/>
        </svg>
        <span>Adventure Riding GPS trails</span>
      </li>
    </ul>
  </article>
</body>
</html>
```